Brovane Website re-design with new logo and look

Refresh on current website. Incorporate new logo which is attached. We provide technology SAAS services to the healthcare space. Current website is at brovane.com but the new name is Brovane.com (see logo) Key considerations are as follows:
1. Incorporate a promo video location. I have a new video coming out similar to this one. https://www.portfolink.net/gallery/41275063/Mobile-Application-Promo
2. Incorporate platform features section. as an example see this website where it has mini screens that call out various features ie; "all in one GCR platform" see webiste https://www.quendly.io/
3. Add some color splash from the log throughout the website
4. Where possible use the text from our website Brovane.com where not possible use lorem ipsum and we will complete
5. use current theme colors
6. Please use your skills to make it more functional and useful and not replicate what we have.

Target Market(s)

Imaging centers and hospitals

Industry/Entity Type

Healthcare

Coding

Coded - Design and coding required

Number of Pages Required

5+ page

Font styles to use
Sans Serif

Requirements
Must have
• Note section in this website that shows features of the platform as you scoll down. See website https://www.quendly.io/
Nice to have
• Professional look only, keep current color scheme but add in some splash of color from the logo
Should not have
• animated characters or cartoon drawings

```html
<!DOCTYPE html>
<html lang="en">
<head>
<meta charset="utf-8">
<title>Brovane — Technology for Healthcare</title>
<link href="https://fonts.googleapis.com/css2?family=Poppins:wght@400;500;600&display=swap" rel="stylesheet">
<style>
:root{
  --teal:#2ab3c1;
  --teal-dark:#1e9fae;
  --teal-soft:#d9f3f6;
  --ink:#1f1f1f;
  --muted:#3c3c3c;
  --night:#1b1b1b;
  --white:#ffffff;
}
*{box-sizing:border-box;margin:0;padding:0}
html,body{width:1200px;height:5199px;overflow:hidden}
body{position:relative;background:var(--white);font-family:'Poppins',sans-serif;color:var(--ink)}
.abs{position:absolute}
.accent{color:var(--teal)}
.btn{position:absolute;display:flex;align-items:center;justify-content:center;border-radius:20px;font-size:12px;font-weight:500;letter-spacing:.3px;color:var(--white)}
.btn-teal{background:var(--teal)}
.btn-dark{background:var(--night)}
.para{position:absolute;font-size:12.5px;line-height:33.5px;color:var(--muted)}
.bubble{position:absolute;border-radius:50%;background:radial-gradient(circle at 35% 35%,#e9f9fb,#bfeaf0)}
.photo{position:absolute}

/* header */
.brand{position:absolute;left:111px;top:36px;display:flex;align-items:center;gap:10px;font-weight:600;font-size:22px;letter-spacing:2px;color:var(--ink)}
.brand-dot{width:28px;height:28px;border-radius:50%;background:var(--teal)}
.nav{position:absolute;top:40px;font-size:12.5px;color:var(--ink)}

/* solutions */
.solutions{position:absolute;left:111px;top:660px;width:978px;height:404px;border-radius:14px;background:linear-gradient(120deg,#2fb9c6,#22a7b6 60%,#2cb4c1)}
.sol-col{position:absolute;top:108px;color:var(--white)}
.sol-col svg{display:block}
.sol-col h4{font-size:15px;font-weight:500;margin-top:32px}
.sol-col p{font-size:12.5px;line-height:30px;margin-top:8px}
.sol-div{position:absolute;top:108px;width:1px;height:180px;background:rgba(255,255,255,.25)}

/* markets */
.market{position:absolute;width:438px;height:258px;border-radius:10px;background:linear-gradient(180deg,#d6f1f5,#ffffff)}
.market .photo{left:16px;top:20px;width:182px;height:197px;border-radius:4px}
.market h4{position:absolute;left:224px;top:40px;font-size:15px;font-weight:500}
.market p{position:absolute;left:224px;top:72px;width:200px;font-size:12.5px;line-height:33.5px;color:var(--muted)}
.market .more{position:absolute;left:224px;top:188px;display:flex;align-items:center;gap:8px;font-size:12.5px;color:var(--teal);text-decoration:underline}

/* features */
.feat-num{position:absolute;font-size:96px;font-weight:600;color:#eef1f3;line-height:1}
.feat-title{position:absolute;font-size:25px;font-weight:500}
.dash{position:absolute;width:437px;height:276px}
.dash .frame{position:absolute;left:6px;top:-6px;width:431px;height:276px;background:var(--teal);border-radius:4px}
.dash svg{position:absolute;left:0;top:0;width:431px;height:276px;background:#f7fcfd;box-shadow:0 2px 10px rgba(0,0,0,.08)}

/* cases */
.case{position:absolute;top:4436px;width:309px;height:329px;border-radius:8px;overflow:hidden}
.case .cap{position:absolute;left:0;right:0;bottom:30px;text-align:center;color:var(--white);font-size:13px;font-weight:500;line-height:30px}
.arrow{position:absolute;top:4586px;width:30px;height:30px;border-radius:50%;display:flex;align-items:center;justify-content:center}

/* footer */
.footer{position:absolute;left:0;top:4852px;width:1200px;height:347px;background:var(--night);color:var(--white)}
.f-col{position:absolute;top:60px}
.f-col h5{font-size:19px;font-weight:500;color:var(--teal);margin-bottom:14px}
.f-col a{display:block;font-size:13.5px;line-height:37.5px;color:var(--white);text-decoration:none}
</style>
</head>
<body>

<!-- header -->
<div class="brand"><span class="brand-dot"></span>BROVANE</div>
<span class="nav accent" style="left:519px">HOME</span>
<span class="nav" style="left:601px">SOLUTIONS</span>
<span class="nav" style="left:722px">MARKETS</span>
<span class="nav" style="left:831px">CASE STUDIES</span>
<div class="btn btn-teal" style="left:968px;top:30px;width:121px;height:36px">GET STARTED</div>

<!-- hero -->
<p class="abs" style="left:111px;top:151px;font-size:15px;font-weight:500">TECHNOLOGY FOR HEALTHCARE</p>
<h1 class="abs" style="left:111px;top:198px;font-size:28px;font-weight:500">REVOLUTIONIZING <span class="accent">HEALTHCARE</span></h1>
<h2 class="abs" style="left:111px;top:252px;font-size:21px;font-weight:500">WITH SEAMLESS TECHNOLOGY</h2>
<p class="para" style="left:111px;top:299px;width:450px">Our end to end workflow platform is purposely built for remote access from anywhere in the world while providing centralized management access.</p>
<div class="btn btn-teal" style="left:111px;top:428px;width:162px;height:38px">REQUEST A DEMO</div>
<p class="abs" style="left:111px;top:499px;font-size:13px;font-weight:500">CALL US : 1-208-555-0147</p>

<div class="bubble" style="left:914px;top:70px;width:206px;height:176px;border-radius:50%"></div>
<div class="bubble" style="left:862px;top:138px;width:10px;height:14px;background:var(--teal)"></div>
<div class="bubble" style="left:627px;top:478px;width:10px;height:14px;background:var(--teal)"></div>
<svg class="abs" style="left:603px;top:76px" width="40" height="80" aria-hidden="true"><g fill="#555"><circle cx="4" cy="4" r="1.5"/><circle cx="14" cy="4" r="1.5"/><circle cx="24" cy="4" r="1.5"/><circle cx="4" cy="14" r="1.5"/><circle cx="14" cy="14" r="1.5"/><circle cx="4" cy="24" r="1.5"/><circle cx="14" cy="24" r="1.5"/><circle cx="4" cy="34" r="1.5"/></g></svg>
<div class="photo" role="img" aria-label="Physician reviewing medical data on a digital display" style="left:612px;top:56px;width:181px;height:216px;border-radius:90px 90px 0 0;background:linear-gradient(160deg,#7ba6c4,#2f4f6e)"></div>
<div class="photo" role="img" aria-label="Healthcare professional working on a laptop in a modern office" style="left:656px;top:192px;width:310px;height:404px;border-radius:0 0 155px 155px;background:linear-gradient(170deg,#3d5e7e,#1f2f47 70%,#2b4460)"></div>
<svg class="abs" style="left:688px;top:506px" width="80" height="80" aria-hidden="true"><path d="M40 4 A36 36 0 1 0 76 40" fill="none" stroke="#222" stroke-width="2"/><path d="M40 14 A26 26 0 1 0 66 40" fill="none" stroke="#222" stroke-width="1.5"/></svg>

<!-- solutions -->
<section class="solutions">
  <h3 class="abs" style="left:0;right:0;top:44px;text-align:center;color:#fff;font-size:22px;font-weight:500">OUR SOLUTIONS</h3>
  <div class="sol-col" style="left:36px">
    <svg width="60" height="58" viewBox="0 0 60 58" fill="none" stroke="#fff" stroke-width="2"><rect x="2" y="2" width="56" height="40" rx="2"/><path d="M22 52h16M30 42v10"/><path d="M30 10v24M22 14c-6 2-8 10-6 16M38 14c6 2 8 10 6 16"/></svg>
    <h4>TELERADIOLOGY</h4><p>End to End workflow to and<br>from anywhere</p>
  </div>
  <div class="sol-div" style="left:272px"></div>
  <div class="sol-col" style="left:309px">
    <svg width="60" height="58" viewBox="0 0 60 58" fill="none" stroke="#fff" stroke-width="2"><rect x="4" y="6" width="36" height="46" rx="2"/><path d="M14 6V2h16v4M10 20h14M10 30h10M10 40h10"/><circle cx="40" cy="34" r="10"/><path d="M47 41l9 9"/></svg>
    <h4>CLINICAL</h4><p>Highly Subspecialized<br>Clinicians</p>
  </div>
  <div class="sol-div" style="left:504px"></div>
  <div class="sol-col" style="left:539px">
    <svg width="60" height="58" viewBox="0 0 60 58" fill="none" stroke="#fff" stroke-width="2"><rect x="4" y="6" width="36" height="46" rx="2"/><path d="M14 6V2h16v4M10 18h6M20 18h12M10 28h6M20 28h12M10 38h6"/><path d="M44 26l14 26H30z"/><path d="M44 35v8M44 46v2"/></svg>
    <h4>COMPLIANCE</h4><p>Integrated compliance<br>across various verticals</p>
  </div>
  <div class="sol-div" style="left:746px"></div>
  <div class="sol-col" style="left:787px">
    <svg width="60" height="58" viewBox="0 0 60 58" fill="none" stroke="#fff" stroke-width="2"><circle cx="14" cy="10" r="6"/><path d="M4 28c0-8 20-8 20 0"/><circle cx="44" cy="34" r="6"/><path d="M34 52c0-8 20-8 20 0"/><path d="M34 8h14v10M44 14l4 4 4-4M24 46H10V36M6 40l4-4 4 4"/></svg>
    <h4>PACS/RIS</h4><p>Affordable PACS/RIS<br>replacement</p>
  </div>
  <div class="btn btn-dark" style="left:422px;top:323px;width:135px;height:36px">LEARN MORE</div>
</section>

<!-- purpose built -->
<div class="abs" style="left:111px;top:1156px;width:434px;height:458px;border:2px solid var(--teal);border-radius:18px"></div>
<div class="photo" role="img" aria-label="Team of medical professionals standing together holding a tablet" style="left:119px;top:1146px;width:426px;height:460px;border-radius:16px;background:linear-gradient(180deg,#c9d3db,#8e9aa6 45%,#2d3540)"></div>
<p class="abs" style="left:603px;top:1192px;font-size:19px;font-weight:500">TECHNOLOGY FOR YOU!</p>
<h2 class="abs" style="left:603px;top:1238px;font-size:26px;font-weight:500"><span class="accent">PURPOSE BUILT</span> TECHNOLOGY</h2>
<p class="para" style="left:603px;top:1289px;width:490px">Lorem ipsum dolor sit amet, consectetur adipiscing elit, sed do eiusmod tempor incididunt ut labore et dolore magna aliqua. Ut enim ad minim veniam, quis nostrud exercitation ullamco laboris nisi ut aliquip ex ea commodo consequat. Duis aute irure dolor in reprehenderit in voluptate velit esse cillum dolore eu fugiat nulla pariatur. Excepteur sint occaecat cupidatat non proident, sunt in culpa qui officia deserunt mollit anim id est laborum.</p>
<div class="btn btn-teal" style="left:603px;top:1550px;width:128px;height:36px">LEARN MORE</div>

<!-- markets -->
<div class="bubble" style="left:40px;top:1699px;width:81px;height:76px"></div>
<div class="bubble" style="left:1101px;top:2306px;width:81px;height:80px"></div>
<p class="abs" style="left:0;width:1200px;top:1694px;text-align:center;font-size:20px;font-weight:500">MARKETS</p>
<h2 class="abs" style="left:0;width:1200px;top:1735px;text-align:center;font-size:27px;font-weight:500"><span class="accent">ADAPTIVE SOLUTIONS FOR</span> EVERY MARKET</h2>

<div class="market" style="left:149px;top:1820px">
  <div class="photo" role="img" aria-label="Nurse assisting an elderly patient in a wheelchair" style="background:linear-gradient(160deg,#cfe0e8,#6fa9c2)"></div>
  <h4>HOSPITALS</h4><p>Lorem Ipsum is simply dummy text of the printing and typesetting industry.</p>
  <span class="more"><svg width="18" height="18" viewBox="0 0 18 18"><circle cx="9" cy="9" r="9" fill="#2ab3c1"/><path d="M5 9h8M9.5 5.5 13 9l-3.5 3.5" stroke="#fff" stroke-width="1.6" fill="none"/></svg>LEARN MORE</span>
</div>
<div class="market" style="left:611px;top:1820px">
  <div class="photo" role="img" aria-label="Clinician caring for a patient in an urgent care room" style="background:linear-gradient(160deg,#dfe7ee,#5c7f9e)"></div>
  <h4>URGENT CARE</h4><p>Lorem Ipsum is simply dummy text of the printing and typesetting industry.</p>
  <span class="more"><svg width="18" height="18" viewBox="0 0 18 18"><circle cx="9" cy="9" r="9" fill="#2ab3c1"/><path d="M5 9h8M9.5 5.5 13 9l-3.5 3.5" stroke="#fff" stroke-width="1.6" fill="none"/></svg>LEARN MORE</span>
</div>
<div class="market" style="left:149px;top:2102px">
  <div class="photo" role="img" aria-label="Hand touching a digital security shield interface" style="background:linear-gradient(160deg,#1d3a5c,#0c1d33)"></div>
  <h4>GOVERNMENT HEALTH</h4><p>Lorem Ipsum is simply dummy text of the printing and typesetting industry.</p>
  <span class="more"><svg width="18" height="18" viewBox="0 0 18 18"><circle cx="9" cy="9" r="9" fill="#2ab3c1"/><path d="M5 9h8M9.5 5.5 13 9l-3.5 3.5" stroke="#fff" stroke-width="1.6" fill="none"/></svg>LEARN MORE</span>
</div>
<div class="market" style="left:611px;top:2102px">
  <div class="photo" role="img" aria-label="Veterinarian examining a dog" style="background:linear-gradient(160deg,#4a4540,#b99a78)"></div>
  <h4>VETERINARIAN</h4><p>Lorem Ipsum is simply dummy text of the printing and typesetting industry.</p>
  <span class="more"><svg width="18" height="18" viewBox="0 0 18 18"><circle cx="9" cy="9" r="9" fill="#2ab3c1"/><path d="M5 9h8M9.5 5.5 13 9l-3.5 3.5" stroke="#fff" stroke-width="1.6" fill="none"/></svg>LEARN MORE</span>
</div>

<!-- promo video -->
<div class="photo" role="img" aria-label="Promo video still: cloud technology concept over a warm blurred background" style="left:111px;top:2407px;width:978px;height:329px;border-radius:6px;background:linear-gradient(100deg,#e7d2bd,#cfe3ea 45%,#bcd9e2 60%,#efd5bf)"></div>
<svg class="abs" style="left:572px;top:2546px" width="56" height="56" viewBox="0 0 56 56" aria-label="Play video"><circle cx="28" cy="28" r="26" fill="#111"/><path d="M22 17l18 11-18 11z" fill="#fff"/></svg>

<!-- features -->
<svg width="0" height="0" style="position:absolute" aria-hidden="true">
  <defs>
    <symbol id="dashboard" viewBox="0 0 431 276">
      <rect width="431" height="276" fill="#f7fcfd"/>
      <rect width="86" height="276" fill="#ffffff"/>
      <circle cx="43" cy="34" r="12" fill="#2ab3c1"/>
      <g fill="#c8e9ee"><rect x="22" y="70" width="44" height="5" rx="2"/><rect x="22" y="110" width="44" height="5" rx="2"/><rect x="22" y="130" width="44" height="5" rx="2"/><rect x="22" y="150" width="44" height="5" rx="2"/><rect x="22" y="250" width="30" height="5" rx="2"/></g>
      <rect x="12" y="86" width="62" height="14" rx="3" fill="#2ab3c1"/>
      <rect x="102" y="12" width="60" height="6" rx="2" fill="#2ab3c1"/>
      <rect x="102" y="24" width="180" height="60" fill="#ffffff"/>
      <g fill="#2ab3c1"><rect x="110" y="60" width="5" height="20"/><rect x="118" y="50" width="5" height="30"/><rect x="126" y="64" width="5" height="16"/><rect x="134" y="44" width="5" height="36"/><rect x="142" y="56" width="5" height="24"/><rect x="150" y="40" width="5" height="40"/><rect x="158" y="58" width="5" height="22"/><rect x="166" y="48" width="5" height="32"/><rect x="174" y="36" width="5" height="44"/><rect x="182" y="52" width="5" height="28"/><rect x="190" y="42" width="5" height="38"/><rect x="198" y="60" width="5" height="20"/><rect x="206" y="34" width="5" height="46"/><rect x="214" y="50" width="5" height="30"/><rect x="222" y="44" width="5" height="36"/><rect x="230" y="56" width="5" height="24"/><rect x="238" y="38" width="5" height="42"/><rect x="246" y="52" width="5" height="28"/><rect x="254" y="46" width="5" height="34"/><rect x="262" y="30" width="5" height="50"/></g>
      <rect x="292" y="24" width="128" height="60" fill="#ffffff"/>
      <g fill="#d4eef2"><rect x="300" y="34" width="16" height="10"/><rect x="320" y="34" width="16" height="10"/><rect x="340" y="34" width="16" height="10"/><rect x="300" y="50" width="16" height="10"/><rect x="320" y="50" width="16" height="10"/><rect x="340" y="50" width="16" height="10"/><rect x="300" y="66" width="16" height="10"/><rect x="320" y="66" width="16" height="10"/></g>
      <g fill="#2ab3c1"><rect x="364" y="34" width="48" height="8"/><rect x="364" y="48" width="48" height="8"/><rect x="364" y="62" width="48" height="8"/></g>
      <rect x="102" y="94" width="230" height="72" fill="#ffffff"/>
      <polyline points="110,140 140,118 170,150 200,124 230,146 260,120 290,152 322,126" fill="none" stroke="#2ab3c1" stroke-width="2"/>
      <polyline points="110,130 140,146 170,124 200,152 230,128 260,150 290,122 322,144" fill="none" stroke="#1f1f1f" stroke-width="1"/>
      <rect x="342" y="94" width="78" height="72" fill="#ffffff"/>
      <circle cx="366" cy="116" r="11" fill="none" stroke="#2ab3c1" stroke-width="4"/>
      <circle cx="366" cy="146" r="11" fill="none" stroke="#2ab3c1" stroke-width="4" stroke-dasharray="40 30"/>
      <g fill="#c8e9ee"><rect x="384" y="112" width="28" height="5"/><rect x="384" y="142" width="28" height="5"/></g>
      <rect x="102" y="176" width="170" height="88" fill="#ffffff"/>
      <g fill="#2ab3c1"><rect x="112" y="226" width="6" height="30"/><rect x="124" y="210" width="6" height="46"/><rect x="136" y="236" width="6" height="20"/><rect x="148" y="216" width="6" height="40"/><rect x="160" y="230" width="6" height="26"/><rect x="172" y="204" width="6" height="52"/><rect x="184" y="222" width="6" height="34"/><rect x="196" y="238" width="6" height="18"/><rect x="208" y="214" width="6" height="42"/><rect x="220" y="228" width="6" height="28"/><rect x="232" y="208" width="6" height="48"/><rect x="244" y="232" width="6" height="24"/><rect x="256" y="218" width="6" height="38"/></g>
      <rect x="282" y="176" width="138" height="88" fill="#ffffff"/>
      <circle cx="320" cy="220" r="24" fill="none" stroke="#2ab3c1" stroke-width="6" stroke-dasharray="110 40"/>
      <circle cx="385" cy="220" r="20" fill="none" stroke="#2ab3c1" stroke-width="6"/>
      <circle cx="385" cy="220" r="8" fill="#2ab3c1"/>
    </symbol>
  </defs>
</svg>

<div class="bubble" style="left:387px;top:3122px;width:81px;height:81px"></div>
<div class="bubble" style="left:938px;top:3486px;width:77px;height:81px"></div>

<h2 class="abs" style="left:0;width:1200px;top:2810px;text-align:center;font-size:27px;font-weight:500"><span class="accent">OUR</span> FEATURES</h2>

<span class="feat-num" style="left:108px;top:2852px">01</span>
<h3 class="feat-title accent" style="left:111px;top:2911px">ALL-IN-ONE GCR PLATFORM</h3>
<p class="para" style="left:111px;top:2958px;width:490px">Lorem ipsum dolor sit amet, consectetur adipiscing elit, sed do eiusmod tempor incididunt ut labore et dolore magna aliqua. Ut enim ad minim veniam, quis nostrud exercitation ullamco laboris nisi ut aliquip ex ea commodo consequat.</p>
<div class="btn btn-teal" style="left:111px;top:3119px;width:127px;height:37px">LEARN MORE</div>
<div class="dash" style="left:652px;top:2901px"><div class="frame"></div><svg role="img" aria-label="Platform dashboard overview"><use href="#dashboard"/></svg></div>

<div class="dash" style="left:111px;top:3270px"><div class="frame"></div><svg role="img" aria-label="Cloud dashboard view"><use href="#dashboard"/></svg></div>
<span class="feat-num" style="left:596px;top:3218px">02</span>
<h3 class="feat-title" style="left:609px;top:3280px">CLOUD-BASED ACCESSIBILITY</h3>
<p class="para" style="left:609px;top:3328px;width:490px">Lorem ipsum dolor sit amet, consectetur adipiscing elit, sed do eiusmod tempor incididunt ut labore et dolore magna aliqua. Ut enim ad minim veniam, quis nostrud exercitation ullamco laboris nisi ut aliquip ex ea commodo consequat.</p>
<div class="btn btn-dark" style="left:609px;top:3488px;width:127px;height:36px">LEARN MORE</div>

<span class="feat-num" style="left:108px;top:3583px">03</span>
<h3 class="feat-title accent" style="left:111px;top:3640px">INTEGRATED DATA SECURITY</h3>
<p class="para" style="left:111px;top:3689px;width:490px">Lorem ipsum dolor sit amet, consectetur adipiscing elit, sed do eiusmod tempor incididunt ut labore et dolore magna aliqua. Ut enim ad minim veniam, quis nostrud exercitation ullamco laboris nisi ut aliquip ex ea commodo consequat.</p>
<div class="btn btn-teal" style="left:111px;top:3849px;width:127px;height:36px">LEARN MORE</div>
<div class="dash" style="left:652px;top:3631px"><div class="frame"></div><svg role="img" aria-label="Data security dashboard view"><use href="#dashboard"/></svg></div>

<!-- call to action -->
<section class="abs" style="left:111px;top:3986px;width:978px;height:251px;border-radius:12px;background:linear-gradient(120deg,#2fb9c6,#22a7b6)">
  <h2 class="abs" style="left:0;right:0;top:55px;text-align:center;color:#fff;font-size:26px;font-weight:500">ARE YOU READY TO <span style="color:var(--ink)">ACCELERATE YOUR BUSINESS?</span></h2>
  <p class="abs" style="left:0;right:0;top:115px;text-align:center;color:#fff;font-size:14px">Give us a call to learn more about what we do at Brovane....</p>
  <div class="btn btn-dark" style="left:403px;top:167px;width:172px;height:37px">GET STARTED NOW</div>
</section>

<!-- case studies -->
<div class="bubble" style="left:71px;top:4303px;width:80px;height:80px"></div>
<p class="abs" style="left:0;width:1200px;top:4318px;text-align:center;font-size:20px;font-weight:500">CASE STUDIES</p>
<h2 class="abs" style="left:0;width:1200px;top:4358px;text-align:center;font-size:27px;font-weight:500"><span class="accent">SUSTAINABILITY</span> SUCCESS STORIES</h2>

<div class="case" role="img" aria-label="Illuminated government office building at dusk" style="left:111px;background:linear-gradient(180deg,#2b3440,#4a3a28 60%,#1a1a1a)"><div class="cap">GOVERNMENT DEPLOYMENT<br>ACROSS 150 LOCATIONS</div></div>
<div class="case" role="img" aria-label="Tablet showing a clinical report chart on a desk" style="left:446px;background:linear-gradient(180deg,#7a7d80,#3a3c40 60%,#1f2022)"><div class="cap">PREDICTIVE CLINICAL REPORTING</div></div>
<div class="case" role="img" aria-label="Professional planning workflows on a glass board" style="left:781px;background:linear-gradient(180deg,#dfe6ee,#7e8fa3 55%,#2a3341)"><div class="cap">CENTRALIZED WORKFLOW<br>MANAGEMENT</div></div>

<div class="arrow" style="left:33px;background:var(--night)"><svg width="14" height="14" viewBox="0 0 14 14"><path d="M9 2 4 7l5 5" stroke="#fff" stroke-width="2" fill="none"/></svg></div>
<div class="arrow" style="left:1125px;background:var(--teal)"><svg width="14" height="14" viewBox="0 0 14 14"><path d="M5 2l5 5-5 5" stroke="#fff" stroke-width="2" fill="none"/></svg></div>

<!-- footer -->
<footer class="footer">
  <div class="abs" style="left:150px;top:60px;width:70px;height:70px;border-radius:50%;background:var(--teal)"></div>
  <p class="abs" style="left:111px;top:186px;font-size:40px;font-weight:500;letter-spacing:4px">BROVANE</p>
  <div class="f-col" style="left:454px"><h5>QUICK LINKS</h5><a>Home</a><a>Solutions</a><a>Markets</a><a>Case Studies</a></div>
  <div class="f-col" style="left:680px"><h5>SOLUTIONS</h5><a>Teleradiology</a><a>Clinical</a><a>Compliance</a><a>PACS/RIS</a></div>
  <div class="f-col" style="left:910px"><h5>MARKETS</h5><a>Hospitals</a><a>Urgent Care</a><a>Government Healthcare</a><a>Veterinarian</a></div>
  <p class="abs" style="left:0;width:1200px;top:306px;text-align:center;font-size:11px">© 2024 <span class="accent">BROVANE</span>. ALL RIGHTS RESERVED</p>
</footer>

</body>
</html>
```